Succession & Estate Planning firm needs a double-sided one page client handout

We need a client hand-out that highlights the top 10 Reasons to get a Pension Plan. It will need the 10 reasons as headings, with a short description of each reason (attached Word doc). It should communicate that a Pension Plan is flexible and provides security. Our usual client is a business owner/medical professional/entrepreneur. Have a look at our website for more info about our business www.marvelko.ca Our logo colours are 83c242, 3b3839, d5d5d5 We like clean, modern, info-graphics, not too cluttered, not too loudWe would like the ability to update the text/content ourselves, in the future.

```html
<!DOCTYPE html>
<html lang="en">
<head>
<meta charset="utf-8">
<title>Top 10 Reasons Why an FPP Serves Your Family Enterprise – Marvelko</title>
<link rel="stylesheet" href="https://fonts.googleapis.com/css2?family=Open+Sans:wght@400;600;700;800&display=swap">
<style>
  :root {
    --brand-green: #83c242;
    --tab-green: #72b83c;
    --ink: #3b3839;
    --body-ink: #2f2d2e;
    --card-grey: #e6e6e6;
    --card-edge: #d5d5d5;
    --page-white: #f4f4f4;
    --back-green: #c3dca6;
    --canvas: #ececec;
  }
  * { box-sizing: border-box; margin: 0; padding: 0; }
  html, body { width: 1200px; height: 1200px; overflow: hidden; }
  body {
    background: var(--canvas);
    font-family: "Open Sans", Arial, sans-serif;
    color: var(--ink);
    position: relative;
  }
  .page {
    position: absolute;
    top: 215px;
    width: 545px;
    height: 770px;
    box-shadow: 0 6px 22px rgba(0,0,0,0.18);
    overflow: hidden;
  }
  .page--front { left: 36px; background: var(--page-white); }
  .page--back { left: 619px; background: var(--back-green); padding: 44px 30px 40px 24px; }

  .hero-photo {
    position: absolute;
    left: 0; right: 0; top: 130px; height: 300px;
    background:
      radial-gradient(ellipse at 70% 45%, rgba(196,140,96,0.55), transparent 55%),
      radial-gradient(ellipse at 20% 80%, rgba(230,180,160,0.6), transparent 50%),
      linear-gradient(180deg, rgba(244,244,244,0) 0%, #e8dcc4 35%, #d9cfae 60%, rgba(244,244,244,0) 100%);
  }
  .brand {
    position: relative;
    display: flex;
    justify-content: center;
    align-items: center;
    gap: 10px;
    padding-top: 34px;
  }
  .brand__name {
    font-size: 30px;
    font-weight: 700;
    color: var(--ink);
  }
  .brand__dot {
    width: 14px; height: 14px; border-radius: 50%;
    background: var(--brand-green);
  }
  .headline {
    position: relative;
    text-align: center;
    font-weight: 800;
    font-size: 30px;
    line-height: 1.12;
    color: var(--brand-green);
    margin-top: 18px;
  }
  .reason-list {
    position: absolute;
    left: 24px; right: 26px; top: 318px;
    display: flex; flex-direction: column; gap: 14px;
  }
  .page--back .reason-list {
    position: static;
    gap: 22px;
  }
  .reason {
    position: relative;
    display: flex;
    min-height: 78px;
  }
  .reason__number {
    flex: 0 0 58px;
    background: var(--tab-green);
    color: #fff;
    font-weight: 800;
    font-size: 30px;
    display: flex; align-items: center; justify-content: center;
    border-radius: 4px 0 0 4px;
    margin-bottom: -8px;
  }
  .reason__card {
    flex: 1;
    background: var(--card-grey);
    border-radius: 0 5px 5px 0;
    box-shadow: 3px 4px 0 var(--card-edge), 4px 6px 10px rgba(0,0,0,0.18);
    padding: 9px 14px 10px 12px;
  }
  .reason__title {
    font-size: 15px;
    font-weight: 700;
    text-transform: uppercase;
    color: var(--body-ink);
    margin-bottom: 3px;
  }
  .reason__text {
    font-size: 10.6px;
    line-height: 1.38;
    color: var(--body-ink);
    text-align: justify;
  }
  .site {
    position: absolute;
    right: 26px; bottom: 12px;
    font-size: 9px;
    color: var(--ink);
  }
</style>
</head>
<body>

<section class="page page--front">
  <div class="hero-photo" role="img" aria-label="Photo of a hand placing a coin beside stacked coins with small green seedlings growing from them"></div>

  <header class="brand">
    <span class="brand__name">Marvelko</span>
    <span class="brand__dot"></span>
  </header>

  <h1 class="headline">Top 10 Reasons<br>Why an FPP Serves Your<br>Family Enterprise</h1>

  <div class="reason-list">
    <article class="reason">
      <div class="reason__number">01</div>
      <div class="reason__card">
        <h2 class="reason__title">Create Significant Deductions</h2>
        <p class="reason__text">The FPP creates significant tax deductions, which can be used to keep the business under the small business rate or applied to the high rate, a bigger bang for the buck.</p>
      </div>
    </article>
    <article class="reason">
      <div class="reason__number">02</div>
      <div class="reason__card">
        <h2 class="reason__title">Deliberate, Planned, Future</h2>
        <p class="reason__text">An income for beyond the last day at the office.</p>
      </div>
    </article>
    <article class="reason">
      <div class="reason__number">03</div>
      <div class="reason__card">
        <h2 class="reason__title">Past Buy Back</h2>
        <p class="reason__text">Most owners invest, first, in the business. The FPP offers the ability to go back and recover lost years when they did not buy RRSPs...and pass the tax savings onto their company.</p>
      </div>
    </article>
    <article class="reason">
      <div class="reason__number">04</div>
      <div class="reason__card">
        <h2 class="reason__title">Creditor Proof</h2>
        <p class="reason__text">All Assets held in an FPP are creditor proof, including RRSPs, and planned pension contributions receive “super-priority” status, which rank above the claims of secured creditors, like major commercial lenders and banks.</p>
      </div>
    </article>
  </div>
  <div class="site">www.marvelko.ca</div>
</section>

<section class="page page--back">
  <div class="reason-list">
    <article class="reason">
      <div class="reason__number">05</div>
      <div class="reason__card">
        <h2 class="reason__title">Flexibility</h2>
        <p class="reason__text">Owners know that cash flows can swing wildly with the business cycle. An FPP offers the flexibility to flip between DB and DC accounts in order to conserve cash, smooth income during volatile years, and recover assets when things improve.</p>
      </div>
    </article>
    <article class="reason">
      <div class="reason__number">06</div>
      <div class="reason__card">
        <h2 class="reason__title">Preserve the Lifetime Capital Gains Exemption</h2>
        <p class="reason__text">Create $1.6 Million++ of Tax Free Capital Gains. The significant deductions created in an FPP can be used to purify a corporation with passive assets, which can help preserve the shareholders’ lifetime capital gains exemption.</p>
      </div>
    </article>
    <article class="reason">
      <div class="reason__number">07</div>
      <div class="reason__card">
        <h2 class="reason__title">Intergenerational Wealth Transfer</h2>
        <p class="reason__text">Unlike RRSPs that eventually trigger a taxable disposition upon death, an FPP has the ability to pass, tax deferred, to the next generation of family business owners.</p>
      </div>
    </article>
    <article class="reason">
      <div class="reason__number">08</div>
      <div class="reason__card">
        <h2 class="reason__title">All Ages</h2>
        <p class="reason__text">An FPP can benefit all entrepreneurs between ages 18-71.</p>
      </div>
    </article>
    <article class="reason">
      <div class="reason__number">09</div>
      <div class="reason__card">
        <h2 class="reason__title">Preserve the Small Business Deduction</h2>
        <p class="reason__text">Passive income inside an FPP grows tax exempt and does not create passive income as outlined under the 2018 “Harlow Measures”. Business owners that redirect corporate resources to fund their FPP will not jeopardize their low corporate tax rate on profits and active companies.</p>
      </div>
    </article>
    <article class="reason">
      <div class="reason__number">10</div>
      <div class="reason__card">
        <h2 class="reason__title">Broader Investment Options</h2>
        <p class="reason__text">An FPP allows entrepreneurs to invest in what they like: real estate, other businesses and/or franchises, private equity, public equity, exempt markets, etc. The possibilities are up to the imagination of the entrepreneur and their advisors.</p>
      </div>
    </article>
  </div>
</section>

</body>
</html>
```